Copper Ridge Resort & Marina - Boat Slips, Cabin Rentals, Floating Vacation Homes, & More

We need an 8'H x 16'W billboard for our Resort & marina, www.copperridgeresort.example. We'd like it to include: Lakefront Cabin Rentals, Floating Vacation Homes, and New Slips Summer 2022. We'd like it to be simple using the colors on our logo, similar to our business cards, and have our logo on it large. Maybe an arrow on the bottom pointing left that says 3 miles, possibly our website and phone number.

Target Market(s)

Lake People, Boaters

Industry/Entity Type

Resort & Marina (Recreation/Hospitality)

Font styles to use
Sans Serif
Other font styles liked:
• Simple/modern

Colors
0054AA
0677BA
7BADD7
CADEEF
E8F1F8
FFC000
F8CF3A
FAE287
FDF2CF
FEFAEE
F0912C
F2A743
F7CA91
FBE8D2
FDF5EE

Requirements
Must have
• Logo, Cabin Rentals, Floating Vacation Homes, New Slips Summer 2022
Nice to have
• An additional banner hanging from the bottom with an orange (or blue, colors from our logo) arrow pointing left, with white text saying: 3 miles 555-214-0867 www.copperridgeresort.example
Should not have
• Shouldn't be too busy

```html
<!DOCTYPE html>
<html lang="en">
<head>
<meta charset="utf-8">
<title>Copper Ridge Resort &amp; Marina Billboard</title>
<link rel="stylesheet" href="https://fonts.googleapis.com/css2?family=Montserrat:wght@400;500;700;800&display=swap">
<style>
  :root {
    --lake-blue: #18498c;
    --sun-orange: #f8b31c;
    --white: #ffffff;
    --page: #eef1f4;
  }
  * { margin: 0; padding: 0; box-sizing: border-box; }
  html, body {
    width: 1200px;
    height: 1031px;
    overflow: hidden;
    background: var(--page);
    font-family: "Montserrat", sans-serif;
  }
  .billboard {
    position: absolute;
    left: 40px;
    top: 231px;
    width: 1120px;
    height: 568px;
    background: var(--lake-blue);
    overflow: hidden;
  }
  .top-stripe {
    position: absolute;
    left: 0; top: 0;
    width: 100%;
    height: 23px;
    background: var(--sun-orange);
  }
  .contact-band {
    position: absolute;
    left: 0; bottom: 0;
    width: 100%;
    height: 78px;
    background: var(--sun-orange);
  }
  .contact-line {
    position: absolute;
    right: 78px;
    top: 50%;
    transform: translateY(-50%);
    color: var(--lake-blue);
    font-weight: 700;
    font-size: 26px;
    letter-spacing: 0.2px;
    white-space: nowrap;
  }
  .lake-map {
    position: absolute;
    left: 28px;
    top: 45px;
    width: 330px;
    height: 370px;
    border-radius: 40px;
    background: radial-gradient(ellipse at 55% 45%, rgba(255,255,255,0.9) 0%, rgba(255,255,255,0.45) 45%, rgba(255,255,255,0) 72%);
  }
  .brand-name {
    position: absolute;
    left: 464px;
    top: 130px;
    width: 500px;
    text-align: center;
    color: var(--white);
    font-weight: 500;
    font-size: 44px;
    line-height: 1.15;
    letter-spacing: 1px;
  }
  .features {
    position: absolute;
    top: 326px;
    left: 0;
    width: 100%;
    height: 110px;
  }
  .feature {
    position: absolute;
    top: 0;
    display: flex;
    align-items: center;
    gap: 10px;
  }
  .feature--cabins { left: 364px; }
  .feature--homes  { left: 601px; }
  .feature--slips  { left: 837px; }
  .tick { width: 44px; height: 44px; flex: none; }
  .feature-text {
    font-size: 29px;
    line-height: 33px;
    color: var(--white);
  }
  .feature-text .lead { display: block; color: var(--sun-orange); font-weight: 500; }
  .feature-text .key  { display: block; font-weight: 700; }
  .feature-text .tail { display: block; font-weight: 400; }
  .distance-sign {
    position: absolute;
    left: 18px;
    top: 444px;
    width: 220px;
    height: 124px;
  }
  .distance-label {
    position: absolute;
    left: 36px;
    top: 10px;
    width: 168px;
    text-align: center;
    color: var(--lake-blue);
    font-weight: 800;
    font-size: 26px;
    line-height: 48px;
    white-space: nowrap;
  }
</style>
</head>
<body>
  <main class="billboard">
    <div class="top-stripe"></div>

    <div class="lake-map" role="img" aria-label="White outline map of the lake with a red star marking the resort location"></div>

    <h1 class="brand-name">Copper Ridge Resort &amp; Marina</h1>

    <section class="features">
      <div class="feature feature--cabins">
        <svg class="tick" viewBox="0 0 44 44" aria-hidden="true">
          <circle cx="22" cy="22" r="18" fill="none" stroke="#f8b31c" stroke-width="4"/>
          <path d="M13 22 l7 7 l14 -15" fill="none" stroke="#f8b31c" stroke-width="5" stroke-linecap="round" stroke-linejoin="round"/>
        </svg>
        <p class="feature-text"><span class="lead">Lakefront</span><span class="key">Cabin</span><span class="tail">Rentals</span></p>
      </div>
      <div class="feature feature--homes">
        <svg class="tick" viewBox="0 0 44 44" aria-hidden="true">
          <circle cx="22" cy="22" r="18" fill="none" stroke="#f8b31c" stroke-width="4"/>
          <path d="M13 22 l7 7 l14 -15" fill="none" stroke="#f8b31c" stroke-width="5" stroke-linecap="round" stroke-linejoin="round"/>
        </svg>
        <p class="feature-text"><span class="lead">Floating</span><span class="key">Vacation</span><span class="tail">Homes</span></p>
      </div>
      <div class="feature feature--slips">
        <svg class="tick" viewBox="0 0 44 44" aria-hidden="true">
          <circle cx="22" cy="22" r="18" fill="none" stroke="#f8b31c" stroke-width="4"/>
          <path d="M13 22 l7 7 l14 -15" fill="none" stroke="#f8b31c" stroke-width="5" stroke-linecap="round" stroke-linejoin="round"/>
        </svg>
        <p class="feature-text"><span class="lead">New Slips</span><span class="key">Summer</span><span class="tail">2022</span></p>
      </div>
    </section>

    <div class="contact-band">
      <p class="contact-line">555-214-0867 | www.copperridgeresort.example</p>
    </div>

    <div class="distance-sign">
      <svg width="220" height="124" viewBox="0 0 220 124" aria-hidden="true">
        <rect x="58" y="60" width="14" height="66" fill="#ffffff" stroke="#18498c" stroke-width="3"/>
        <rect x="144" y="60" width="14" height="66" fill="#ffffff" stroke="#18498c" stroke-width="3"/>
        <path d="M4 34 L34 4 H214 L202 34 L214 64 H34 Z" fill="#ffffff" stroke="#18498c" stroke-width="4" stroke-linejoin="round"/>
      </svg>
      <span class="distance-label">3 MILES</span>
    </div>
  </main>
</body>
</html>
```